CPA, Management and IT Consulting Redesign Existing Website

We currently have a website that is outdated (www.qelvarn.com). We need a good website developer that can redesign our website. To make this easier I have chosen a few websites that we like the layout or template. Use our exiting website content for this project. Our new logo is attached below. Based on who wins this we will upgrade to a coded website and a content management system (CMS) so we can make changes to the text ourselves in the future.

http://www.brontekhaile.com/
http://www.lorvicanmanagement.com/

Target Market(s)

Government Clients

Industry/Entity Type

Management Consulting

Number of Pages Required

5+ page

Font styles to use
Serif

Requirements
Must have
• Please the following website templates as a guide.
• http://www.brontekhaile.com/
• http://www.lorvicanmanagement.com/
Nice to have
Should not have

```html
<!DOCTYPE html>
<html lang="en">
<head>
<meta charset="utf-8">
<title>Qelvarn Enterprises, LLC</title>
<link rel="stylesheet" href="https://fonts.googleapis.com/css2?family=Hind:wght@400;500;600;700&family=Roboto:wght@400;500;700&display=swap">
<style>
:root{
  --orange:#f9a03a;
  --dark:#333333;
  --nav:#2b2b2b;
  --ink:#222222;
  --text:#3a3a3a;
  --grey-bg:#ececec;
  --card-border:#c9c9c9;
  --white:#ffffff;
  --photo-a:#cfdbe6;
  --photo-b:#eef2f5;
}
*{box-sizing:border-box;margin:0;padding:0}
html,body{width:1200px;height:2571px;overflow:hidden}
body{font-family:"Roboto",Arial,sans-serif;color:var(--text);background:var(--white);position:relative}
.abs{position:absolute}
a{color:inherit;text-decoration:none}

/* header */
.site-header{position:absolute;left:0;top:0;width:1200px;height:125px;background:var(--orange)}
.brand-panel{position:absolute;left:0;top:0;width:390px;height:125px}
.brand{position:absolute;left:48px;top:28px;display:flex;align-items:center;gap:14px}
.brand-mark{width:52px;height:62px;background:var(--orange)}
.brand-name{font-family:"Hind",sans-serif;font-weight:700;color:var(--ink);font-size:29px;line-height:30px;letter-spacing:.5px}
.contact-item{position:absolute;top:22px;display:flex;gap:14px;color:var(--white)}
.contact-item h4{font-family:"Roboto",sans-serif;font-weight:500;font-size:20px;line-height:24px}
.contact-item p{font-size:13.5px;line-height:17px}
.social-strip{position:absolute;left:900px;top:106px;width:300px;height:46px;z-index:3}
.social-list{position:absolute;left:50px;top:8px;display:flex;gap:10px}
.social-list span{width:30px;height:30px;border:2px solid var(--ink);border-radius:50%}

/* nav */
.main-nav{position:absolute;left:0;top:125px;width:1200px;height:52px;background:var(--nav)}
.main-nav a{position:absolute;top:17px;color:var(--white);font-family:"Hind",sans-serif;font-weight:500;font-size:15.5px;letter-spacing:.3px}

/* hero */
.hero-photo{position:absolute;left:0;top:177px;width:1200px;height:483px;background:linear-gradient(120deg,var(--photo-a),var(--photo-b) 55%,#d9e3ea)}

/* about */
.about{position:absolute;left:0;top:660px;width:1200px;height:300px;text-align:center}
.section-title{font-family:"Hind",sans-serif;font-weight:600;font-size:30px;letter-spacing:.5px;color:var(--ink)}
.section-title .accent{color:var(--orange)}
.about .section-title{position:absolute;top:30px;width:100%}
.about p{position:absolute;left:90px;width:1020px;font-size:17.5px;line-height:23px;color:var(--ink)}

/* quick cards */
.quick-links{position:absolute;left:0;top:960px;width:1200px;height:351px;background:var(--grey-bg)}
.quick-card{position:absolute;top:31px;width:334px;height:288px;border:2px solid var(--card-border);text-align:center}
.quick-card.is-active{border-color:var(--orange)}
.quick-card svg{position:absolute;left:127px;top:16px}
.quick-card h3{position:absolute;top:112px;width:100%;font-family:"Roboto",sans-serif;font-weight:400;font-size:20px;color:var(--ink)}
.quick-card ul{position:absolute;top:160px;width:100%;list-style:none;font-size:15px;line-height:27px;color:var(--ink)}

/* services */
.services{position:absolute;left:0;top:1311px;width:1200px;height:477px;background:var(--orange);color:var(--white)}
.services .section-title{position:absolute;top:40px;width:100%;text-align:center;color:var(--white);font-size:28px}
.title-rule{position:absolute;left:565px;top:82px;width:70px;height:3px;background:var(--white)}
.service{position:absolute;top:140px;width:280px;text-align:center}
.service .icon{margin:0 auto;width:94px;height:94px;border:2px solid var(--white);border-radius:50%;display:flex;align-items:center;justify-content:center}
.service h3{margin-top:22px;font-family:"Roboto",sans-serif;font-weight:700;font-size:16px}
.service p{margin:14px auto 0;width:240px;font-size:13.5px;line-height:23px}
.btn-more{display:inline-block;margin-top:28px;width:98px;height:36px;line-height:34px;border:1.5px solid var(--white);font-size:12.5px;letter-spacing:.5px}

/* testimonials */
.testimonials{position:absolute;left:0;top:1788px;width:1200px;height:440px;text-align:center;color:var(--ink)}
.testimonials .section-title{position:absolute;top:36px;width:100%;font-size:28px}
.quote-badge{position:absolute;left:562px;top:106px;width:76px;height:76px;border-radius:50%;background:#6a6a6a}
.quote-text{position:absolute;left:115px;top:177px;width:970px;font-size:15px;line-height:23px}
.quote-by{position:absolute;top:318px;width:100%;font-family:"Hind",sans-serif;font-weight:600;font-size:14px}
.quote-name{position:absolute;top:342px;width:100%;font-family:"Hind",sans-serif;font-weight:700;font-size:14px;letter-spacing:.6px}
.slider-dots{position:absolute;left:497px;top:393px;display:flex;gap:4px}
.slider-dots span{width:36px;height:5px;background:var(--dark)}
.slider-dots span.is-current{background:var(--orange)}

/* footer */
.site-footer{position:absolute;left:0;top:2228px;width:1200px;height:278px;background:var(--dark);color:var(--white)}
.footer-col{position:absolute;top:0;height:278px;padding-top:40px}
.footer-col + .footer-col{border-left:1px solid #3d3d3d}
.footer-col h4{font-family:"Roboto",sans-serif;font-weight:500;font-size:20px;margin-bottom:20px}
.footer-col ul{list-style:none;font-size:14px;line-height:29px}
.footer-col.links li::before{content:"";display:inline-block;width:0;height:0;border-left:5px solid var(--white);border-top:4px solid transparent;border-bottom:4px solid transparent;margin-right:7px;vertical-align:1px}
.legal{position:absolute;left:0;top:2506px;width:1200px;height:65px;background:var(--orange);color:var(--white);text-align:center;font-size:13px;line-height:20px;padding-top:12px}
</style>
</head>
<body>

<header class="site-header">
  <svg class="brand-panel" width="390" height="125" viewBox="0 0 390 125"><polygon points="0,0 335,0 380,62 335,125 0,125" fill="#fff"/></svg>
  <div class="brand">
    <div class="brand-mark"></div>
    <div class="brand-name">QELVARN<br>ENTERPRISES, LLC</div>
  </div>

  <div class="contact-item" style="left:505px">
    <svg width="30" height="44" viewBox="0 0 30 44"><path d="M15 0C6.7 0 0 6.7 0 15c0 11 15 29 15 29s15-18 15-29C30 6.7 23.3 0 15 0zm0 21a6 6 0 1 1 0-12 6 6 0 0 1 0 12z" fill="#222"/></svg>
    <div><h4>Address</h4><p>2417 M Street NW, Suite 410<br>Washington</p></div>
  </div>
  <div class="contact-item" style="left:765px">
    <svg width="40" height="40" viewBox="0 0 40 40"><circle cx="20" cy="20" r="18" fill="none" stroke="#222" stroke-width="3"/><path d="M13 11l4 0 2 5-3 2c1 3 3 5 6 6l2-3 5 2 0 4c-9 1-17-7-16-16z" fill="#222"/></svg>
    <div><h4>Call Us</h4><p>(202) 555-0148</p></div>
  </div>
  <div class="contact-item" style="left:962px">
    <svg width="40" height="40" viewBox="0 0 40 40"><circle cx="20" cy="20" r="18" fill="none" stroke="#222" stroke-width="3"/><rect x="10" y="13" width="20" height="14" fill="none" stroke="#222" stroke-width="2.5"/><path d="M10 13l10 8 10-8" fill="none" stroke="#222" stroke-width="2.5"/></svg>
    <div><h4>Email Address</h4><p>info@qelvarn.com</p></div>
  </div>
</header>

<div class="social-strip" aria-label="Social links">
  <svg class="abs" width="300" height="46" viewBox="0 0 300 46"><polygon points="20,0 300,0 300,46 20,46 0,23" fill="#fff"/></svg>
  <div class="social-list"><span></span><span></span><span></span><span></span><span></span></div>
</div>

<nav class="main-nav">
  <a href="#" style="left:80px">HOME</a>
  <a href="#" style="left:189px">ABOUT US</a>
  <a href="#" style="left:327px">SERVICES</a>
  <a href="#" style="left:461px">INDUSTRIES</a>
  <a href="#" style="left:613px">CONTACT US</a>
</nav>

<div class="hero-photo" role="img" aria-label="Photo of a consulting team meeting around a table in a bright office"></div>

<section class="about">
  <h2 class="section-title">ABOUT <span class="accent">QELVARN ENTERPRISES</span></h2>
  <p style="top:82px">Qelvarn Enterprises, LLC and Ashby &amp; Corwell, LLC is a network of certified public accounting and management consulting firms with seasoned professionals and an excellent reputation for serving a diverse client base including federal agencies, state and local government, non-profit organizations, small and medium-sized business entities, professional associations and individuals.</p>
  <p style="top:198px">We are committed to professional excellence across all service areas including Audit and Assurance, Accounting, Tax, Management Consulting, and Information Technology.</p>
</section>

<section class="quick-links">
  <div class="quick-card is-active" style="left:48px">
    <svg width="80" height="84" viewBox="0 0 80 84"><circle cx="40" cy="56" r="24" fill="none" stroke="#222" stroke-width="4"/><path d="M16 56h48M40 32v48M22 44h36M22 68h36" stroke="#222" stroke-width="3"/><circle cx="22" cy="12" r="7" fill="#222"/><circle cx="40" cy="10" r="8" fill="#222"/><circle cx="58" cy="12" r="7" fill="#222"/><path d="M10 38c0-12 24-12 24 0zM28 38c0-14 24-14 24 0zM46 38c0-12 24-12 24 0z" fill="#222"/></svg>
    <h3>Services and Solutions</h3>
    <ul><li>Audit, Accounting and Tax</li><li>Financial Management</li><li>Information Technology</li><li>Governance, Risk and Compliance</li></ul>
  </div>
  <div class="quick-card" style="left:432px">
    <svg width="80" height="84" viewBox="0 0 80 84"><path d="M4 78V40l14-8v8l14-8v8l14-8V10h8v-6h8v6h8v68z" fill="none" stroke="#222" stroke-width="3"/><g fill="none" stroke="#222" stroke-width="2"><rect x="12" y="50" width="8" height="6"/><rect x="24" y="50" width="8" height="6"/><rect x="36" y="50" width="8" height="6"/><rect x="48" y="50" width="8" height="6"/><rect x="60" y="50" width="8" height="6"/><rect x="12" y="62" width="8" height="6"/><rect x="24" y="62" width="8" height="6"/><rect x="36" y="62" width="8" height="6"/><rect x="48" y="62" width="8" height="6"/><rect x="60" y="62" width="8" height="6"/></g></svg>
    <h3>Industries</h3>
    <ul><li>Federal Government</li><li>State and Local Government</li><li>Financial Services</li><li>Not-for-Profit</li></ul>
  </div>
  <div class="quick-card" style="left:816px">
    <svg width="80" height="84" viewBox="0 0 80 84"><g fill="none" stroke="#222" stroke-width="2"><circle cx="14" cy="12" r="6"/><circle cx="30" cy="10" r="6"/><circle cx="50" cy="10" r="6"/><circle cx="66" cy="12" r="6"/><path d="M4 34c0-14 20-14 20 0M20 32c0-14 20-14 20 0M40 32c0-14 20-14 20 0M56 34c0-14 20-14 20 0"/></g><circle cx="40" cy="56" r="20" fill="#111"/><text x="40" y="65" text-anchor="middle" font-family="Roboto,sans-serif" font-weight="700" font-size="26" fill="#fff">?</text></svg>
    <h3>About Us</h3>
    <ul><li>Company Overview</li><li>Management</li><li>Clients</li><li>Careers</li></ul>
  </div>
</section>

<section class="services">
  <h2 class="section-title">OUR SERVICES</h2>
  <div class="title-rule"></div>

  <div class="service" style="left:31px">
    <div class="icon"><svg width="40" height="50" viewBox="0 0 40 50"><text x="20" y="42" text-anchor="middle" font-family="Roboto,sans-serif" font-weight="700" font-size="46" fill="#fff">$</text></svg></div>
    <h3>Financial Management</h3>
    <p>We offer a full range of assurance services that translates numbers into accurate, meaningful information for quality decision-making.</p>
    <a class="btn-more" href="#">READ MORE</a>
  </div>
  <div class="service" style="left:319px">
    <div class="icon"><svg width="34" height="44" viewBox="0 0 34 44"><rect x="2" y="2" width="30" height="40" rx="3" fill="none" stroke="#fff" stroke-width="2.5"/><rect x="7" y="7" width="20" height="8" fill="#fff"/><g fill="#fff"><rect x="7" y="19" width="5" height="4"/><rect x="15" y="19" width="5" height="4"/><rect x="23" y="19" width="5" height="4"/><rect x="7" y="26" width="5" height="4"/><rect x="15" y="26" width="5" height="4"/><rect x="23" y="26" width="5" height="4"/><rect x="7" y="33" width="5" height="4"/><rect x="15" y="33" width="5" height="4"/><rect x="23" y="33" width="5" height="4"/></g></svg></div>
    <h3>Accounting, Audit and Tax</h3>
    <p>We offer a full range of assurance services that translates numbers into accurate, meaningful information for quality decision-making.</p>
    <a class="btn-more" href="#">READ MORE</a>
  </div>
  <div class="service" style="left:609px">
    <div class="icon"><svg width="40" height="44" viewBox="0 0 40 44"><path d="M4 2h20l8 8v30H4z" fill="none" stroke="#fff" stroke-width="2.5"/><path d="M9 16h16M9 22h12M9 28h10" stroke="#fff" stroke-width="2"/><circle cx="30" cy="32" r="8" fill="var(--orange)" stroke="#fff" stroke-width="2.5"/><path d="M30 29v7" stroke="#fff" stroke-width="2.5"/></svg></div>
    <h3>Information Technology</h3>
    <p>We offer a full range of assurance services that translates numbers into accurate, meaningful information for quality decision-making.</p>
    <a class="btn-more" href="#">READ MORE</a>
  </div>
  <div class="service" style="left:895px">
    <div class="icon"><svg width="40" height="46" viewBox="0 0 40 46"><rect x="3" y="5" width="28" height="36" rx="2" fill="none" stroke="#fff" stroke-width="2.5"/><rect x="11" y="2" width="12" height="6" fill="#fff"/><path d="M8 16h18M8 22h14M8 28h10" stroke="#fff" stroke-width="2"/><circle cx="30" cy="34" r="8" fill="var(--orange)" stroke="#fff" stroke-width="2.5"/><path d="M26 34l3 3 5-6" fill="none" stroke="#fff" stroke-width="2.5"/></svg></div>
    <h3>Governance, Risk &amp; Compliance</h3>
    <p>We offer a full range of assurance services that translates numbers into accurate, meaningful information for quality decision-making.</p>
    <a class="btn-more" href="#">READ MORE</a>
  </div>
</section>

<section class="testimonials">
  <h2 class="section-title">OUR TESTIMONIALS</h2>
  <div class="quote-badge"><svg width="76" height="76" viewBox="0 0 76 76"><path d="M26 28h10v10c0 6-3 10-8 11l-1-3c3-1 4-3 4-6h-5zM42 28h10v10c0 6-3 10-8 11l-1-3c3-1 4-3 4-6h-5z" fill="#fff"/></svg></div>
  <p class="quote-text">"Tuvera help us to find new potential customers and also to deepen existing customer relationships. Scent desire to customize exactly to our needs service tool has been ihaltavaa "Tuvera help us to find new potential customers and also to deepen existing customer relationships. Scent desire to customize exactly to our needs service tool has been ihaltavaa""</p>
  <p class="quote-by">Written By</p>
  <p class="quote-name">JUSSI HALMEKOSKI, SALES MANAGER, NORVENDA LTD</p>
  <div class="slider-dots"><span class="is-current"></span><span></span><span></span><span></span><span></span></div>
</section>

<footer class="site-footer">
  <div class="footer-col" style="left:0;width:305px;padding-left:65px">
    <h4>Contact Us</h4>
    <ul><li>2417 M Street NW, Suite 410</li><li>Washington, DC 20006</li><li>Phone: (202) 555-0148</li><li>Fax: (202) 555-0193</li><li>Email: info@qelvarn.com</li></ul>
  </div>
  <div class="footer-col links" style="left:305px;width:317px;padding-left:17px">
    <h4>Services and Solutions</h4>
    <ul><li>Audit, Accounting and Tax</li><li>Financial Management</li><li>Information Technology</li><li>Governance, Risk and Compliance</li></ul>
  </div>
  <div class="footer-col links" style="left:605px;width:257px;padding-left:17px">
    <h4>Industries</h4>
    <ul><li>Federal Government</li><li>State and Local Government</li><li>Financial Services</li><li>Not-for-Profit</li></ul>
  </div>
  <div class="footer-col links" style="left:862px;width:338px;padding-left:28px">
    <h4>About Us</h4>
    <ul><li>Company Overview</li><li>Management</li><li>Clients</li><li>Careers</li></ul>
  </div>
</footer>

<div class="legal">
  <p>Privacy Policy | Cookie Policy | Conditions of Use | Notice and Take Down Policy | Powered by Pellora</p>
  <p>© 2016. The content on this website is owned by us and our licensors. Do not copy any content (including images) without our consent.</p>
</div>

</body>
</html>
```